The Brambury Firm

We need a new design for our letterhead and envelopes. We are a personal injury and criminal defense firm so we need something modern and clean, but more on the professional/traditional side. Our new logo has two colors and is attached to the file so we need something that works well with those colors/matches the design. The following information needs to be on the letterhead:
Phone: (555) 314-7265
Fax: (555) 419-6032
Toll-Free: (555) 736-1149
Post Office Box 4273
Marlow Bend, TQ 29458-4273
TQHarmClaimsDesk.example
PalmettoShieldCounsel.example

Target Market(s)

Clients, government agencies, other law firms

Industry/Entity Type

Legal

Font styles to use
Sans Serif
Other font styles liked:
• Arial

Colors

Designer to choose colors to be used in the design.

Requirements
Must have
• Must look professional and clean, modern
Nice to have
• I would like to see a design that works with the logo but does not distract from the content that will be printed on it
Should not have
• Too many colors or crazy designs.

```html
<!DOCTYPE html>
<html lang="en">
<head>
<meta charset="utf-8">
<title>The Brambury Firm — Envelope</title>
<link href="https://fonts.googleapis.com/css2?family=Arimo:wght@400;700&display=swap" rel="stylesheet">
<style>
  :root {
    --backdrop: #e6e7e8;
    --paper: #ffffff;
    --navy: #2e3192;
    --brand-red: #c8202f;
    --ink: #1a1a1a;
    --guide: #8a8c8e;
  }
  html, body {
    margin: 0;
    padding: 0;
    width: 1200px;
    height: 1200px;
    overflow: hidden;
    background: var(--backdrop);
  }
  .artboard { display: block; width: 1200px; height: 1200px; }
  .envelope-body { fill: var(--paper); }
  .envelope-flap { fill: var(--navy); }
  .guide { stroke: var(--guide); stroke-width: 0.6; fill: none; }
  .wordmark {
    font-family: "Arimo", Arial, sans-serif;
    font-weight: 700;
    font-size: 15px;
    fill: var(--brand-red);
  }
  .contact {
    font-family: "Arimo", Arial, sans-serif;
    font-size: 6.8px;
    fill: var(--ink);
  }
</style>
</head>
<body>
<svg class="artboard" viewBox="0 0 1200 1200" xmlns="http://www.w3.org/2000/svg">
  <!-- envelope -->
  <rect class="envelope-body" x="365.6" y="484.8" width="476.8" height="249.6"/>
  <polygon class="envelope-flap" points="365.6,484.8 842.4,484.8 818.4,530.4 389.6,530.4"/>

  <!-- layout guides -->
  <g class="guides">
    <line class="guide" x1="389.6" y1="438.4" x2="389.6" y2="760"/>
    <line class="guide" x1="406.4" y1="438.4" x2="406.4" y2="760"/>
    <line class="guide" x1="604" y1="438.4" x2="604" y2="760"/>
    <line class="guide" x1="686.4" y1="438.4" x2="686.4" y2="760"/>
    <line class="guide" x1="801.6" y1="438.4" x2="801.6" y2="760"/>
    <line class="guide" x1="818.4" y1="438.4" x2="818.4" y2="760"/>
    <line class="guide" x1="348" y1="664" x2="852.8" y2="664"/>
    <line class="guide" x1="348" y1="690.4" x2="852.8" y2="690.4"/>
    <rect class="guide" x="389.6" y="584" width="16.8" height="16.8"/>
    <rect class="guide" x="801.6" y="584" width="16.8" height="16.8"/>
    <rect class="guide" x="825.6" y="717.6" width="16.8" height="16.8"/>
  </g>

  <!-- firm name -->
  <text class="wordmark" x="406.4" y="683">The Brambury Firm</text>

  <!-- phone column -->
  <g class="contact">
    <text x="604" y="670">P: (555) 314-7265</text>
    <text x="604" y="679">F: (555) 419-6032</text>
    <text x="604" y="696">T-F: (555) 736-1149</text>
  </g>

  <!-- address column -->
  <g class="contact">
    <text x="686.4" y="670">Post Office Box 4273</text>
    <text x="686.4" y="679">Marlow Bend, TQ 29458-4273</text>
    <text x="686.4" y="695.5">www.TQHarmClaimsDesk.example</text>
    <text x="686.4" y="704" textLength="112" lengthAdjust="spacingAndGlyphs">www.PalmettoShieldCounsel.example</text>
  </g>
</svg>
</body>
</html>
```